Commercial Construction Company Looking to Revamp Image

Varnholt Construction Co., Inc. has been in business for 20 years, and is a mid sized commercial construction company looking to update our image to reflect a more modern corporate culture, but to still reflect traditional core values in construction, such as dependability, honesty, and solid workmanship. Our largest clients include government and public agencies who seek companies with the aforementioned values, but are open to new ideas and innovations. We have used a dark blue and white to represent us in the past and would like for this color scheme to continue as not to isolate our existing customers. The addition of a gray is acceptable. Please see our previous business card. *It is imperative to retain the logo as closely as possible.* There is a possibility to shorten the name of the company to "VCCI," dependent on design concepts, or possible integration of the acronym to our existing name.

Industry/Entity Type

Business

```html
<!DOCTYPE html>
<html lang="en">
<head>
<meta charset="utf-8">
<title>Varnholt Construction Co., Inc. — Business Card</title>
<link href="https://fonts.googleapis.com/css2?family=Poiret+One&display=swap" rel="stylesheet">
<style>
  :root {
    --brand-blue: #1433d6;
    --ink-blue: #1b3fd8;
    --stage-blue: #1230d6;
    --stage-deep: #0a1f9a;
    --card-white: #ffffff;
    --card-gray: #e4e6e8;
  }
  html, body {
    margin: 0;
    padding: 0;
    overflow: hidden;
  }
  body {
    width: 1200px;
    height: 1000px;
    position: relative;
    background: var(--stage-blue);
    font-family: "Poiret One", "Trebuchet MS", sans-serif;
    color: var(--ink-blue);
  }
  .card {
    position: absolute;
    width: 860px;
    height: 460px;
    background: linear-gradient(160deg, var(--card-white) 60%, var(--card-gray) 100%);
    box-shadow: 0 0 40px 8px var(--stage-deep);
  }
  .card--front { left: 315px; top: 30px; }
  .card--back  { left: 36px;  top: 517px; }

  .brand-mark {
    position: absolute;
    display: flex;
    align-items: center;
    gap: 14px;
    transform: translateX(-50%);
  }
  .brand-mark__square {
    background: var(--brand-blue);
    flex: none;
  }
  .brand-mark__name {
    color: var(--brand-blue);
    font-weight: 400;
    letter-spacing: 2px;
    white-space: nowrap;
  }
  .card--front .brand-mark { left: 433px; top: 150px; }
  .card--front .brand-mark__square { width: 86px; height: 86px; }
  .card--front .brand-mark__name { font-size: 64px; }
  .card--back .brand-mark { left: 426px; top: 40px; }
  .card--back .brand-mark__square { width: 60px; height: 60px; }
  .card--back .brand-mark__name { font-size: 44px; }

  .company {
    position: absolute;
    text-align: center;
    line-height: 1;
    white-space: nowrap;
    transform: translateX(-50%);
  }
  .company__line { display: block; }
  .company__suffix { letter-spacing: 0; }

  .card--front .company { left: 436px; top: 312px; }
  .card--front .company__line--first { font-size: 48px; letter-spacing: 1px; }
  .card--front .company__line--second { font-size: 52px; margin-top: 8px; }
  .card--front .company__suffix { font-size: 32px; }

  .card--back .company { left: 424px; top: 178px; }
  .card--back .company__line--first { font-size: 28px; letter-spacing: 1px; }
  .card--back .company__line--second { font-size: 30px; margin-top: 3px; }
  .card--back .company__suffix { font-size: 20px; }

  .person {
    position: absolute;
    left: 424px;
    top: 250px;
    transform: translateX(-50%);
    text-align: center;
    font-size: 54px;
    line-height: 66px;
    white-space: nowrap;
  }
  .contact {
    position: absolute;
    top: 18px;
    font-size: 17px;
    line-height: 22px;
    white-space: nowrap;
  }
  .contact--address { left: 11px; }
  .contact--address .indent { padding-left: 6px; }
  .contact--phones { right: 34px; text-align: center; top: 24px; }
</style>
</head>
<body>

<section class="card card--front" aria-label="Card front">
  <div class="brand-mark">
    <span class="brand-mark__square"></span>
    <span class="brand-mark__name">VCCI</span>
  </div>
  <h1 class="company" style="margin:0;font-weight:400">
    <span class="company__line company__line--first">VARNHOLT</span>
    <span class="company__line company__line--second">CONSTRUCTION <span class="company__suffix">CO., INC</span></span>
  </h1>
</section>

<section class="card card--back" aria-label="Card back">
  <address class="contact contact--address" style="font-style:normal">
    1180 Harlow Street<br>
    <span class="indent">Bayview, N.J. 07002</span><br>
    varnholtconstruction@mailbox.com
  </address>
  <div class="brand-mark">
    <span class="brand-mark__square"></span>
    <span class="brand-mark__name">VCCI</span>
  </div>
  <div class="contact contact--phones">
    Office: (201) 555-0142<br>
    Fax: (201) 555-0187<br>
    Cell: (917) 555-0123
  </div>
  <div class="company">
    <span class="company__line company__line--first">VARNHOLT</span>
    <span class="company__line company__line--second">CONSTRUCTION <span class="company__suffix">CO., INC</span></span>
  </div>
  <div class="person">
    <div class="person__name">Marek Varnholt</div>
    <div class="person__title">President</div>
  </div>
</section>

</body>
</html>
```